"Psychic / Tarot Card Reader / Healer Needs a Web Page Design

We need a web page design for company that does psychic / tarot card readings / healings etc.
It currently has 6 different tabs which include: Home, testimonials, service, certificates, contact us plus a shop where if people want to they can purchase services on line.
Should be mystical / magic like yet simple.
Will upload a copy of the current logo for the business.
It's name is Velvet Lantern.

Target Market(s)

spiritual

Industry/Entity Type

It Company

Number of Pages Required

5+ page

```html
<!DOCTYPE html>
<html lang="en">
<head>
<meta charset="utf-8">
<title>Velvet Lantern — Psychic, Healer &amp; Tarot Card Reader</title>
<link href="https://fonts.googleapis.com/css2?family=Raleway:wght@400;500;600;700&family=Roboto:wght@300;400;500;700&display=swap" rel="stylesheet">
<style>
:root{
  --purple:#7d1f8a;
  --purple-deep:#561063;
  --magenta:#a0309f;
  --ink:#222222;
  --text:#666666;
  --light:#f4f4f4;
  --dark:#151515;
  --footer:#252525;
  --footer-bar:#1a1a1a;
  --white:#ffffff;
}
*{margin:0;padding:0;box-sizing:border-box}
html,body{width:1200px;height:3629px;overflow:hidden}
body{font-family:"Roboto",sans-serif;color:var(--text);background:var(--white);position:relative}
section,header,footer{position:absolute;left:0;width:1200px}
.abs{position:absolute}
h2.section-title{font-family:"Raleway",sans-serif;font-weight:500;font-size:30px;letter-spacing:1px;text-align:center;color:var(--ink);position:absolute;left:0;width:1200px}

/* header */
.site-header{top:0;height:116px;background:var(--white)}
.brand{left:88px;top:36px;display:flex;align-items:center;gap:10px;font-family:"Raleway",sans-serif;font-weight:700;font-size:26px;color:var(--purple)}
.brand-dot{width:16px;height:16px;border-radius:50%;background:var(--purple)}
.main-nav{left:350px;top:40px;display:flex;align-items:center;gap:26px;font-family:"Raleway",sans-serif;font-size:15px;color:#444}
.main-nav a{color:inherit;text-decoration:none}
.main-nav .active{color:var(--purple);border:1.5px solid var(--purple);border-radius:20px;padding:6px 16px}
.header-social{left:994px;top:44px;display:flex;gap:10px}
.header-social span{width:20px;height:20px;background:#444;border-radius:3px}

/* hero */
.hero{top:116px;height:690px;overflow:hidden}
.hero-photo{position:absolute;inset:0;background:radial-gradient(ellipse at 52% 30%,#6a4a6a 0%,#2b1c35 40%,#120c1c 80%)}
.hero-lamp{position:absolute;left:20px;top:140px;width:190px;height:440px;background:linear-gradient(180deg,#2a3a4a,#3c5a7a 50%,#3a2a24);border-radius:40px 40px 10px 10px;opacity:.7}
.hero-title{left:0;width:1200px;top:285px;text-align:center;font-family:"Raleway",sans-serif;font-weight:500;font-size:58px;color:var(--white);letter-spacing:1px}
.hero-sub{left:0;width:1200px;top:365px;text-align:center;font-family:"Raleway",sans-serif;font-weight:500;font-size:28px;color:var(--white)}
.hero-arrow{top:330px}
.hero-curve{position:absolute;left:0;bottom:0}

/* welcome */
.welcome{top:806px;height:275px}
.welcome .section-title{top:36px}
.welcome-text{left:130px;width:940px;top:90px;text-align:center;font-size:13px;line-height:22px}
.btn-outline{left:526px;top:175px;width:148px;height:52px;border-radius:26px;border:1px solid #ccc;box-shadow:0 2px 6px rgba(0,0,0,.15);font-size:15px;color:#444;display:flex;align-items:center;justify-content:center}

/* services */
.services{top:1081px;height:462px;background:linear-gradient(90deg,var(--purple-deep),var(--magenta) 50%,var(--purple) 100%)}
.service{position:absolute;top:75px;width:240px;height:330px;text-align:center;color:var(--white)}
.service-photo{width:184px;height:184px;border-radius:50%;border:5px solid var(--white);margin:0 auto}
.service h3{font-family:"Roboto",sans-serif;font-weight:400;font-size:17px;margin-top:26px}
.service p{font-size:12px;line-height:18px;margin-top:10px;opacity:.9}
.service .more{position:absolute;left:0;width:240px;top:305px;font-size:12px}

/* about */
.about{top:1543px;height:402px}
.about h2{left:90px;top:95px;font-family:"Raleway",sans-serif;font-weight:500;font-size:28px;color:var(--ink)}
.about-text{left:90px;top:142px;width:540px;font-size:13px;line-height:21px}
.about .more{left:90px;top:307px;font-size:13px;color:var(--purple)}
.about-video{left:658px;top:78px;width:452px;height:258px;border:4px solid #eee;box-shadow:0 2px 8px rgba(0,0,0,.2);background:linear-gradient(135deg,#3a2a22,#8a6a50 45%,#2a1e1a)}
.play{position:absolute;left:196px;top:99px}

/* blog */
.blog{top:1945px;height:556px;background:radial-gradient(ellipse at 50% 40%,#3a2a2e,var(--dark) 80%)}
.blog .section-title{top:60px;color:var(--white)}
.blog-sub{left:0;width:1200px;top:110px;text-align:center;font-size:16px;color:var(--white)}
.blog-card{position:absolute;top:160px;width:314px;height:343px;background:var(--white)}
.blog-photo{height:187px;margin:6px 6px 0;position:relative}
.date{position:absolute;left:8px;top:42px;width:52px;height:68px;background:var(--purple);color:var(--white);text-align:center;font-size:17px;padding-top:8px;line-height:20px}
.date small{display:block;font-size:10px}
.year{position:absolute;left:8px;top:114px;font-size:13px;color:var(--white)}
.blog-card h3{text-align:center;font-family:"Roboto",sans-serif;font-weight:500;font-size:13px;color:var(--ink);margin-top:18px}
.blog-card p{text-align:center;font-size:12px;line-height:18px;margin:8px 26px 0}
.blog-card .more{text-align:center;font-size:12px;color:var(--purple);margin-top:12px}

/* shop */
.shop{top:2501px;height:513px}
.shop .section-title{top:60px}
.shop-tile{position:absolute;top:131px;width:248px;height:324px}
.shop-feature{background:radial-gradient(ellipse at 50% 40%,#2a3552,#131a2e);color:var(--white);text-align:center}
.shop-feature h3{font-family:"Roboto",sans-serif;font-weight:400;font-size:14px;margin-top:112px}
.shop-feature p{font-size:11px;line-height:16px;margin:6px 30px 0}
.shop-feature .view{display:inline-block;margin-top:10px;font-size:15px;text-decoration:underline}
.shop-icons{display:flex;justify-content:center;gap:16px;margin-top:14px}
.shop-icons span{width:32px;height:32px;border-radius:50%;background:#3a4260;display:flex;align-items:center;justify-content:center}

/* testimonials */
.testimonials{top:3014px;height:305px;background:linear-gradient(90deg,var(--purple-deep),var(--magenta) 50%,var(--purple))}
.testimonials .section-title{top:44px;color:var(--white)}
.avatar{position:absolute;width:108px;height:108px;border-radius:50%;border:4px solid var(--white)}
.quote{position:absolute;color:var(--white);font-size:12px;line-height:19px}
.quote cite{display:block;font-style:italic;font-size:10px;font-weight:700;margin-top:10px;letter-spacing:.3px}

/* footer */
.site-footer{top:3319px;height:310px;background:var(--footer);color:#cfcfcf}
.footer-col{position:absolute;top:52px;font-size:12px;line-height:18px}
.footer-col h4{font-family:"Roboto",sans-serif;font-weight:500;font-size:14px;color:var(--white);margin-bottom:18px;letter-spacing:.5px}
.contact-line{display:flex;align-items:center;gap:10px;margin-top:12px}
.tweet{display:flex;gap:10px;width:250px}
.tweet-icon{flex:none;width:18px;height:18px;background:var(--white);border-radius:3px}
.news-form{display:flex;margin-top:14px}
.news-form .field{width:172px;height:40px;background:var(--white);color:#999;font-size:11px;padding:12px 10px}
.news-form .btn{width:84px;height:40px;background:var(--purple);color:var(--white);font-size:14px;display:flex;align-items:center;justify-content:center}
.social-squares{display:flex;gap:14px}
.social-squares span{width:30px;height:30px;background:var(--white);border-radius:3px}
.footer-bar{position:absolute;left:0;top:225px;width:1200px;height:85px;background:var(--footer-bar);text-align:center;font-size:12px;color:#ddd;padding-top:34px}
</style>
</head>
<body>

<header class="site-header">
  <div class="abs brand"><span class="brand-dot"></span>Velvet Lantern</div>
  <nav class="abs main-nav">
    <a class="active" href="#">HOME</a>
    <a href="#">TESTIMONIALS</a>
    <a href="#">SERVICE</a>
    <a href="#">CERTIFICATES</a>
    <a href="#">CONTACT</a>
    <a href="#">SHOP</a>
  </nav>
  <div class="abs header-social" aria-label="Social links"><span></span><span></span><span></span></div>
</header>

<section class="hero">
  <div class="hero-photo" role="img" aria-label="Photo of a fortune teller in a jewelled headscarf against a dark smoky background"></div>
  <div class="hero-lamp" role="img" aria-label="Ornate glowing lantern"></div>
  <h1 class="abs hero-title">VELVET LANTERN</h1>
  <p class="abs hero-sub">Psychic, Healer &amp; Tarot Card Reader</p>
  <svg class="abs hero-arrow" style="left:72px" width="16" height="30" viewBox="0 0 16 30"><path d="M13 3 3 15l10 12" fill="none" stroke="#fff" stroke-width="3"/></svg>
  <svg class="abs hero-arrow" style="left:1112px" width="16" height="30" viewBox="0 0 16 30"><path d="M3 3l10 12L3 27" fill="none" stroke="#fff" stroke-width="3"/></svg>
  <svg class="hero-curve" width="1200" height="160" viewBox="0 0 1200 160">
    <path d="M0 0 Q300 20 600 145 Q900 20 1200 0 V160 H0Z" fill="#ffffff"/>
  </svg>
</section>

<section class="welcome">
  <h2 class="section-title">WELCOME TO VELVET LANTERN</h2>
  <p class="abs welcome-text">Maren has undertaken various training courses to give herself an indepth knowledge and understanding of Tarot and Reiki whilst applying her intuition to provide her clients with indepth readings. She aims to offer clients guidance and support in any area of their life through the use of these methods. When providing Readings and Reiki Healings, Maren will use her skills and intuition to pass on accurate messages to clients from Heavenly Beings who wish their words</p>
  <div class="abs btn-outline">View More</div>
</section>

<section class="services">
  <div class="service" style="left:90px">
    <div class="service-photo" style="background:radial-gradient(circle,#4a6ab0,#2a1e4a)" role="img" aria-label="Hands laying out angel tarot cards"></div>
    <h3>Angel Card Tarot Readings</h3>
    <p>Celtic Cross Readings are used to give the client a more indepth reading on current situations within their</p>
    <div class="more">Read More ▸</div>
  </div>
  <div class="service" style="left:350px">
    <div class="service-photo" style="background:radial-gradient(circle,#6a5a8a,#1e1a2e)" role="img" aria-label="Healer holding a crystal ball"></div>
    <h3>Reiki Healings</h3>
    <p>Reiki is a healing technique that uses the energy of the universe to heal your mind, body or spirit. It enhances</p>
    <div class="more">Read More ▸</div>
  </div>
  <div class="service" style="left:615px">
    <div class="service-photo" style="background:radial-gradient(circle,#e8c8d8,#b47aa8)" role="img" aria-label="Hands reaching toward soft light"></div>
    <h3>Realm Readings</h3>
    <p>Do you feel like you have a Global Purpose for being on Earth but can't explain it. Then this type of reading</p>
    <div class="more">Read More ▸</div>
  </div>
  <div class="service" style="left:880px">
    <div class="service-photo" style="background:radial-gradient(circle,#5a8ad8,#3a1a5a)" role="img" aria-label="Glowing blue crystal ball"></div>
    <h3>Dream Interpretation</h3>
    <p>Are you dreams trying to send you a message? Our dreams carry many symbolisms and actually provide us</p>
    <div class="more">Read More ▸</div>
  </div>
</section>

<section class="about">
  <h2 class="abs">ABOUT US</h2>
  <p class="abs about-text">You can contact Velvet Lantern at anytime, if you are unable to make contact leave your details and Maren will get back to you as soon as possible. Office Hours are Monday - Friday. If a weekend appointment is required please phone Maren to discuss. Please take into consideration though that with a young family, appointments may need to be rescheduled from time to time. Thank you for you understanding in this matter and I apologise in advance for any inconvenience. Readings via email will generally be conducted in the evening and sent to clients upon completion.</p>
  <div class="abs more">Read More ▸</div>
  <div class="abs about-video" role="img" aria-label="Video still of candles and a hand resting on a table">
    <svg class="play" width="60" height="60" viewBox="0 0 60 60"><circle cx="30" cy="30" r="29" fill="rgba(255,255,255,.35)"/><path d="M24 18 42 30 24 42Z" fill="#333"/></svg>
  </div>
</section>

<section class="blog">
  <h2 class="section-title">LATEST BLOG</h2>
  <p class="abs blog-sub">Neque porro quisquam est qui dolorem ipsum quia dolor sit amet,</p>
  <article class="blog-card" style="left:97px">
    <div class="blog-photo" style="background:linear-gradient(135deg,#c23a2a,#5a2a1a 60%,#2a1a14)" role="img" aria-label="Fortune teller in red scarf with cards">
      <div class="date">02<small>JUN</small></div><div class="year">2017</div>
    </div>
    <h3>NEQUE PORRO QUISQUAM</h3>
    <p>It has survived not only five centuries, but also the leap into electronic typesetting, remaining essentially unchanged</p>
    <div class="more">Read More &gt;</div>
  </article>
  <article class="blog-card" style="left:444px">
    <div class="blog-photo" style="background:linear-gradient(135deg,#3a1a2a,#b02a3a 55%,#2a1a1a)" role="img" aria-label="Red candle among tarot cards">
      <div class="date">02<small>JUN</small></div><div class="year">2017</div>
    </div>
    <h3>QUISQUAM EST DOLOREM</h3>
    <p>It has survived not only five centuries, but also the leap into electronic typesetting, remaining essentially unchanged</p>
    <div class="more">Read More &gt;</div>
  </article>
  <article class="blog-card" style="left:793px">
    <div class="blog-photo" style="background:linear-gradient(135deg,#2a1a12,#a0602a 55%,#3a2212)" role="img" aria-label="Crystal ball among lit candles">
      <div class="date">02<small>JUN</small></div><div class="year">2017</div>
    </div>
    <h3>PORRO QUISQUAM</h3>
    <p>It has survived not only five centuries, but also the leap into electronic typesetting, remaining essentially unchanged</p>
    <div class="more">Read More &gt;</div>
  </article>
</section>

<section class="shop">
  <h2 class="section-title">SHOP</h2>
  <div class="shop-tile shop-feature" style="left:92px">
    <h3>DREAM INTERPRETATION</h3>
    <p>Are you dreams trying to send you messages and you know this</p>
    <span class="view">View More</span>
    <div class="shop-icons">
      <span><svg width="14" height="14" viewBox="0 0 14 14"><path d="M1 2h2l2 7h7l1-5H4" fill="none" stroke="#fff" stroke-width="1.5"/><circle cx="6" cy="12" r="1" fill="#fff"/><circle cx="11" cy="12" r="1" fill="#fff"/></svg></span>
      <span><svg width="14" height="14" viewBox="0 0 14 14"><circle cx="6" cy="6" r="4" fill="none" stroke="#fff" stroke-width="1.5"/><path d="M9 9l4 4" stroke="#fff" stroke-width="1.5"/></svg></span>
    </div>
  </div>
  <div class="shop-tile" style="left:353px;background:linear-gradient(180deg,#3a7ac8,#8ab8e8 50%,#1e3a7a)" role="img" aria-label="Angel tarot card deck box"></div>
  <div class="shop-tile" style="left:612px;background:radial-gradient(ellipse at 50% 50%,#3a5ab0,#0e1230 75%)" role="img" aria-label="Meditating figure with glowing chakra points"></div>
  <div class="shop-tile" style="left:871px;background:linear-gradient(180deg,#e8ecf0,#b0a8c0 50%,#5a3a7a)" role="img" aria-label="Portrait of a Reiki master with calligraphy"></div>
</section>

<section class="testimonials">
  <h2 class="section-title">TESTIMONIALS</h2>
  <div class="avatar" style="left:90px;top:139px;background:radial-gradient(circle,#c84a3a,#5a1a1a)" role="img" aria-label="Client portrait"></div>
  <p class="quote" style="left:213px;top:140px;width:372px">“ Thank you for this wonderous reading. Wow, it's magical and makes perfect sense to me. The reading is beautifully explained. I love the reading. You are extremely gifted with a clear sense of the person ”<cite>LENA ORTIZ - ANGEL CARD TAROT READING</cite></p>
  <div class="avatar" style="left:665px;top:139px;background:radial-gradient(circle,#f0d8b0,#c89a6a)" role="img" aria-label="Client portrait"></div>
  <p class="quote" style="left:782px;top:140px;width:404px">“ Thank you so much for this gorgeous reading! You are a natural girl! This has brought me so much joy and encouragement, as well as affirmation. Thank you, thank you!! Sending you so much love. ”<cite>PRIYA HALE - ANGEL CARD TAROT READING</cite></p>
</section>

<footer class="site-footer">
  <div class="footer-col" style="left:87px">
    <h4>CONTACT US</h4>
    <div>Unit #4, 82 Willow Lane<br>Maple Ridge, BC V2X 3K8</div>
    <div class="contact-line" style="margin-top:20px"><svg width="14" height="14" viewBox="0 0 14 14"><path d="M3 1l3 3-2 2c1 2 2 3 4 4l2-2 3 3-2 2C6 13 1 8 1 3Z" fill="#fff"/></svg><span style="font-size:16px;color:#fff">0400 555 217</span></div>
    <div class="contact-line"><svg width="16" height="12" viewBox="0 0 16 12"><rect x="1" y="1" width="14" height="10" fill="none" stroke="#fff"/><path d="M1 1l7 6 7-6" fill="none" stroke="#fff"/></svg><span>maren@velvetlantern.example</span></div>
  </div>
  <div class="footer-col" style="left:360px">
    <h4>LATEST TWEET'S</h4>
    <div class="tweet"><span class="tweet-icon"></span><span>Phasellus porta. Fusce suscipit varius mi. Cum sociis natoque penatibus et magnis dis parturient montes, nascetur ridiculus mus. See more here http://lnk.example/vl42</span></div>
  </div>
  <div class="footer-col" style="left:668px;width:260px">
    <h4>NEWSLETTER</h4>
    <div>Excepteur sint occaecat cupidatat non proident, sunt in culpa qui officia deserunt mollit anim</div>
    <div class="news-form"><span class="field">Enter your email address</span><span class="btn">Sign Up</span></div>
  </div>
  <div class="footer-col" style="left:973px">
    <h4>SOCIAL MEDIA</h4>
    <div class="social-squares"><span></span><span></span><span></span></div>
  </div>
  <div class="footer-bar">2017 All Rights Reserved.</div>
</footer>

</body>
</html>
```